どんな物をいくらで貸してくれるのかを知りたいお客様が多く、チラシでアピールしたいと思っています。
まずはメイン商品であるぐるっと稜線セットDX、のびのび高原セット、わいわい焚火セット、ゆるりと星祭セットのセット商品の紹介をしたいです。
その他として個々のレンタル品に関して、こんなものも貸してますという紹介を行いたく、例えば登山テント、寝袋、大型ザック、望遠鏡、釣りセット、BBQセットもそれぞれいくらで貸していますという紹介をサブとして紹介したいです。
最後に店舗紹介という形でお願いいたします。
アウトドアギアレンタルこかげどう/TEL:0544-61-3917,FAX:0544-61-3918/店舗地図/ホームページ、http://www.kokagedou.jp/ぐるっと稜線セットDX 9980~、のびのび高原縦走セット 11980~、わいわい焚火セット 12480円、ゆるりと星祭セット 9800円/ロゴ(添付ファイル)
B4
片面
特にありません
アウトドア雑誌のミルフォさんのようなイメージで製作して頂けたらと思います。

デザインとしてはどれも素晴らしい作品でした。その中で、当選させて頂いた作品は、こちらの言葉足らずな部分を補うように、訴えたかった点を表現して頂いた所を評価させて頂きました。

短時間の中で、沢山の提案本当にありがとうございました。
それぞれ良い部分がありましたので選定で悩みました。
またどうぞ宜しくお願いいたします。

```html
<!DOCTYPE html>
<html lang="ja">
<head>
<meta charset="utf-8">
<title>こかげどう レンタルチラシ</title>
<link href="https://fonts.googleapis.com/css2?family=M+PLUS+Rounded+1c:wght@500;700;800&family=Noto+Sans+JP:wght@400;500;700&display=swap" rel="stylesheet">
<style>
:root{
  --paper:#ffffff;
  --ink:#3a3a3a;
  --panel:#d7eef6;
  --panel-edge:#b5dcea;
  --price:#d8262f;
  --teal:#2aa59b;
  --blue:#2a8fd1;
  --orange:#ef8a1f;
  --pink:#e8558f;
  --green:#6fb43a;
  --brand:#5a3a20;
  --rule:#9ccbe0;
}
*{margin:0;padding:0;box-sizing:border-box}
html,body{width:836px;height:1200px;overflow:hidden;background:var(--paper)}
body{font-family:"Noto Sans JP",sans-serif;color:var(--ink);position:relative}
.photo{position:absolute}
.photo-hero{left:0;top:0;width:404px;height:502px;background:linear-gradient(180deg,#dfe9ee 0%,#c9c2a0 45%,#9a8656 100%)}
.photo-tents{left:410px;top:0;width:175px;height:173px;background:linear-gradient(160deg,#c7ccc4,#7d8a6a)}
.photo-peak{left:591px;top:0;width:245px;height:173px;background:linear-gradient(180deg,#3d78c7 0%,#8fb6e3 55%,#eef3f8 100%)}
.photo-hiker{left:410px;top:179px;width:231px;height:156px;background:linear-gradient(180deg,#7fa5c8,#3e5a6e)}
.photo-river{left:647px;top:179px;width:189px;height:156px;background:linear-gradient(160deg,#3f7a35,#5fb4c9)}
.photo-crowd{left:410px;top:341px;width:426px;height:161px;background:linear-gradient(180deg,#d7dde2,#8b8880)}

.headline{position:absolute;top:552px;left:0;width:836px;text-align:center;font-family:"M PLUS Rounded 1c",sans-serif;font-weight:800;font-size:42px;letter-spacing:2px;color:var(--ink)}
.headline .c1{color:var(--teal)}
.headline .c2{color:var(--blue)}
.headline .c3{color:var(--orange)}
.headline .c4{color:var(--pink)}
.headline .c5{color:var(--green)}
.headline .sm{font-size:34px}

.set-panel{position:absolute;left:106px;top:636px;width:624px;height:214px;background:var(--panel);border:2px solid var(--panel-edge);border-radius:6px;padding:14px 26px 0 22px}
.set-row{display:flex;align-items:center;height:46px;font-size:17px;font-weight:500}
.set-icon{width:30px;height:30px;margin-right:12px;flex:none}
.set-name{white-space:nowrap}
.leader{flex:1;border-bottom:2px dotted #7aa9bd;margin:0 8px;transform:translateY(2px)}
.fee-label{font-size:13px;margin-right:10px}
.price{color:var(--price);font-weight:700;font-size:24px;width:120px;white-space:nowrap}

.others-badge{position:absolute;left:48px;top:884px;width:72px;height:72px;border-radius:50%;background:var(--blue);color:#fff;font-size:14px;font-weight:700;line-height:1.25;display:flex;align-items:center;justify-content:center;text-align:center}
.item-grid{position:absolute;left:150px;top:882px;list-style:none;display:grid;grid-template-columns:240px 210px 220px;row-gap:20px;font-size:17px}
.item{white-space:nowrap}
.item::before{content:"";display:inline-block;width:8px;height:8px;border-radius:50%;background:var(--teal);margin-right:8px;transform:translateY(-2px)}

.divider{position:absolute;left:28px;top:998px;width:780px;border-top:2px solid var(--rule)}

.brand{position:absolute;left:36px;top:1032px;width:190px;color:var(--brand);font-family:"M PLUS Rounded 1c",sans-serif;font-weight:800}
.brand-sub{font-size:12px;letter-spacing:1px;white-space:nowrap}
.brand-name{font-size:36px;line-height:1.15;white-space:nowrap}
.contact{position:absolute;left:238px;top:1036px;width:384px;font-weight:700;color:var(--ink)}
.contact-line{display:flex;align-items:center;gap:7px;font-size:20px;white-space:nowrap}
.tag{display:inline-block;background:var(--green);color:#fff;font-size:12px;padding:1px 5px;border-radius:3px}
.contact-phone{margin-right:12px}
.url{font-size:18px;margin-top:14px;letter-spacing:.5px;white-space:nowrap}
.shop-map{position:absolute;left:636px;top:1016px;width:172px;height:120px;background:linear-gradient(135deg,#f2efe6,#dfe8d6);border:1px solid #c8c8c8}
</style>
</head>
<body>
<div class="photo photo-hero" role="img" aria-label="草原でキャンプを楽しむ女性たちの写真"></div>
<div class="photo photo-tents" role="img" aria-label="林間のキャンプ場に並ぶテントの写真"></div>
<div class="photo photo-peak" role="img" aria-label="青空にそびえる雪をかぶった山の写真"></div>
<div class="photo photo-hiker" role="img" aria-label="山頂で景色を眺める登山者の写真"></div>
<div class="photo photo-river" role="img" aria-label="緑に囲まれた清流の写真"></div>
<div class="photo photo-crowd" role="img" aria-label="登山道を歩く人々の写真"></div>

<h1 class="headline"><span class="c1">お手軽</span><span class="c2">レンタル</span><span class="sm">で</span><span class="c3">楽し</span><span class="c4">く</span><span class="c5">アウトドア</span></h1>

<section class="set-panel">
  <div class="set-row">
    <svg class="set-icon" viewBox="0 0 30 30"><circle cx="15" cy="15" r="13" fill="var(--teal)"/></svg>
    <span class="set-name">「ぐるっと稜線セットDX」</span><span class="leader"></span>
    <span class="fee-label">レンタル料</span><span class="price">¥9,980~</span>
  </div>
  <div class="set-row">
    <svg class="set-icon" viewBox="0 0 30 30"><path d="M2 26 L15 5 L28 26 Z" fill="var(--blue)"/></svg>
    <span class="set-name">「のびのび高原縦走セット」</span><span class="leader"></span>
    <span class="fee-label">レンタル料</span><span class="price">¥11,980~</span>
  </div>
  <div class="set-row">
    <svg class="set-icon" viewBox="0 0 30 30"><path d="M2 25 L15 6 L28 25 Z" fill="var(--orange)"/><path d="M13 25 L15 16 L17 25 Z" fill="#fff"/></svg>
    <span class="set-name">「わいわい焚火セット」</span><span class="leader"></span>
    <span class="fee-label">レンタル料</span><span class="price">¥12,480~</span>
  </div>
  <div class="set-row">
    <svg class="set-icon" viewBox="0 0 30 30"><circle cx="10" cy="22" r="6" fill="var(--pink)"/><rect x="14" y="4" width="3" height="18" fill="var(--pink)"/><path d="M17 4 Q24 6 25 13 Q21 9 17 9 Z" fill="var(--pink)"/></svg>
    <span class="set-name">「ゆるりと星祭セット」</span><span class="leader"></span>
    <span class="fee-label">レンタル料</span><span class="price">¥9,800~</span>
  </div>
</section>

<div class="others-badge">他にも<br>あります!</div>
<ul class="item-grid">
  <li class="item">登山テント…¥0000</li>
  <li class="item">寝袋…¥0000</li>
  <li class="item">大型ザック…¥0000</li>
  <li class="item">望遠鏡…¥0000</li>
  <li class="item">釣りセット…¥0000</li>
  <li class="item">BBQセット…¥0000</li>
</ul>

<div class="divider"></div>

<div class="brand">
  <div class="brand-sub">アウトドアギアレンタル</div>
  <div class="brand-name">こかげどう</div>
</div>
<div class="contact">
  <div class="contact-line"><span class="tag">TEL</span><span class="contact-phone">0544-61-3917</span><span class="tag">FAX</span><span>0544-61-3918</span></div>
  <div class="url">http://www.kokagedou.jp/</div>
</div>
<div class="shop-map" role="img" aria-label="店舗周辺の案内地図"></div>
</body>
</html>
```